Investment Management Model Portfolio PDF Flyer

Our clients are retirees and soon-to-be retirees looking for help managing their investment portfolio. Our company designed model portfolios that offer more customization options than competitors' model portfolios. We want to show potential clients that we can provide customization (i.e. "tilts") that allow personalization. Clients can opt for portfolios with more dividends, international exposure, socially-responsible ESG choices, and anything inbetween. Unlike competitors our approach is not one-size-fits-all.

The process of building a portfolio lends itself to metaphors or pictures to do with: building a custom portfolio (DIY-friendly), global diversification (accessing global markets instead of just local markets), and environmentally & socially responsible options (clean energy, rain forest)

Target Market(s)

Seniors (age 65+), retired persons, investors

Industry/Entity Type

Financial Planning

Font styles to use
Serif
Other font styles liked:
• Rufina Bold, Rufina

Colors
ec1f27
0356a4

Requirements
Must have
• -Must use color palette in attached PDF
-Must use pie chart / doughnut chart to represent asset allocation
-At least 4 "asset allocations" for basic benchmark (20/80, 40/60, 60/40, 80/20)
-At least 3 "tilts" are described as Dividend, ESG, and International
Nice to have
• -Asset allocations can be named: conservative, conservative growth, moderate, and growth (20/80, 40/60, 60/40, 80/20, respectively)
-Dividend paying, international and ESG could be represented in pictures or graphics (dividends = money returned to client, international could show a globe or try to represent global markets/currency, ESG is often connected to environmental causes but not only)
Should not have
• -Projected rates of returns

```html
<!DOCTYPE html>
<html lang="en">
<head>
<meta charset="utf-8">
<title>Personalize Your Portfolio Flyer</title>
<link href="https://fonts.googleapis.com/css2?family=Cinzel:wght@400;600&family=Source+Sans+3:wght@400;600;700&display=swap" rel="stylesheet">
<style>
:root{
  --red:#c21f2f;
  --red-soft:#c9614f;
  --red-deep:#8e2f2a;
  --blue:#4a78b5;
  --green:#8cc63f;
  --purple:#6a4f8f;
  --ink:#111;
  --white:#fff;
  --page:#e9e6e2;
}
*{box-sizing:border-box;margin:0;padding:0}
html,body{width:1200px;height:810px;overflow:hidden;background:var(--page)}
body{font-family:"Source Sans 3",sans-serif;color:var(--ink)}
.flyer{position:absolute;left:294px;top:9px;width:612px;height:792px;background:var(--white);overflow:hidden;box-shadow:0 2px 10px rgba(0,0,0,.15)}
.hero{position:absolute;left:0;top:0;width:612px;height:272px}
.hero-photo{position:absolute;inset:0;background:linear-gradient(90deg,#3b3430 0%,#6d5440 40%,#e9a451 62%,#b8743c 80%,#6b4a30 100%)}
.hero-shapes{position:absolute;inset:0}
.headline{position:absolute;left:32px;top:118px;font-family:"Cinzel",serif;font-weight:400;font-size:28px;line-height:31px;color:var(--white);letter-spacing:.5px}
.intro{position:absolute;left:0;top:272px;width:612px;height:124px;background:linear-gradient(90deg,#101010,#2a2a2a 50%,#0d0d0d);color:var(--white);font-size:12.2px;line-height:15.8px;padding:26px 22px 0 27px}
.section-bar{position:absolute;left:0;height:25px;background:var(--ink);color:var(--white);font-family:"Cinzel",serif;font-weight:600;font-size:13px;line-height:25px;padding-left:27px;clip-path:polygon(0 0,100% 0,calc(100% - 10px) 100%,0 100%)}
.bar-split{top:424px;width:296px}
.bar-tilt{top:555px;width:296px}
.split-charts{position:absolute;left:0;top:462px;width:370px;height:90px}
.tilt-charts{position:absolute;left:0;top:593px;width:370px;height:120px}
.chart-title{font-size:6px;fill:var(--ink);text-anchor:middle;font-family:"Source Sans 3",sans-serif}
.legend{font-size:3.6px;fill:var(--ink);font-family:"Source Sans 3",sans-serif}
.pct{font-size:5px;fill:var(--white);font-weight:700;text-anchor:middle;font-family:"Source Sans 3",sans-serif}
.pct-small{font-size:4px}
.dots{fill:var(--blue)}
.freedom{position:absolute;left:370px;top:412px;width:230px;height:313px;background:var(--red);color:var(--white);padding:17px 10px 0 10px}
.freedom h2{font-family:"Cinzel",serif;font-weight:400;font-size:16px;line-height:18px;text-align:center;letter-spacing:.4px;margin-bottom:24px}
.freedom p{font-size:11.2px;line-height:14.4px;text-align:justify;margin-bottom:14px}
.rule{position:absolute;left:0;top:723px;width:612px;height:3px;background:var(--red)}
.brand{position:absolute;left:32px;top:748px;display:flex;align-items:center;gap:8px}
.brand-mark{width:14px;height:14px;border-radius:50%;background:var(--blue)}
.brand-name{font-family:"Source Sans 3",sans-serif;font-weight:600;font-size:20px;color:var(--ink);line-height:1}
.contact{position:absolute;left:370px;top:726px;width:230px;height:66px;background:var(--red);color:var(--white);text-align:center;padding-top:14px}
.phone{font-family:"Cinzel",serif;font-size:16px;display:flex;align-items:center;justify-content:center;gap:4px}
.web{font-size:13.5px;margin-top:4px}
</style>
</head>
<body>
<main class="flyer">
  <section class="hero">
    <div class="hero-photo" role="img" aria-label="Photo of a retired couple embracing, seen from behind, in a field at golden sunset"></div>
    <svg class="hero-shapes" width="612" height="272" viewBox="0 0 612 272">
      <polygon points="0,0 145,0 200,78 0,272" fill="var(--red-deep)" opacity=".85"/>
      <polygon points="145,0 282,0 200,78" fill="var(--red-soft)"/>
      <polygon points="0,272 200,78 390,272" fill="#2b2622" opacity=".55"/>
    </svg>
    <h1 class="headline">PERSONALIZE<br>YOUR<br>PORTFOLIO</h1>
  </section>

  <p class="intro">Lorem ipsum dolor sit amet, consectetuer adipiscing elit, sed diam nonummy nibh euismod tincidunt ut laoreet dolore magna aliquam erat volutpat. Ut wisi enim ad minim veniam, quis nostrud exerci tation ullamcorper suscipit lobortis nisl ut aliquip ex ea commodo consequat. Duis autem vel eum iriure dolor in hendrerit in vulputate velit esse molestie consequat, vel illum dolore eu feugiat nulla facilisis at vero eros et accumsan et iusto odio dignissim qui blandit praesent luptatum zzril</p>

  <h3 class="section-bar bar-split">START WITH STOCK/BOND SPLIT</h3>
  <svg class="split-charts" width="370" height="90" viewBox="0 0 370 90">
    <g transform="translate(56,0)">
      <text class="chart-title" x="0" y="6">20/80</text>
      <circle cx="-12" cy="12" r="1.5" fill="var(--blue)"/><text class="legend" x="-9" y="13.3">Stocks</text>
      <circle cx="4" cy="12" r="1.5" fill="var(--red)"/><text class="legend" x="7" y="13.3">Bonds</text>
      <g transform="translate(0,48) rotate(-90)">
        <circle r="22" fill="none" stroke="var(--blue)" stroke-width="15" pathLength="100" stroke-dasharray="20 100"/>
        <circle r="22" fill="none" stroke="var(--red)" stroke-width="15" pathLength="100" stroke-dasharray="80 100" stroke-dashoffset="-20"/>
      </g>
      <text class="pct" x="13" y="32">20%</text><text class="pct" x="-13" y="67.5">80%</text>
    </g>
    <g class="dots"><circle cx="95" cy="48" r="1.2"/><circle cx="99" cy="48" r="1.2"/><circle cx="103" cy="48" r="1.2"/></g>
    <g transform="translate(144,0)">
      <text class="chart-title" x="0" y="6">40/60</text>
      <circle cx="-12" cy="12" r="1.5" fill="var(--blue)"/><text class="legend" x="-9" y="13.3">Stocks</text>
      <circle cx="4" cy="12" r="1.5" fill="var(--red)"/><text class="legend" x="7" y="13.3">Bonds</text>
      <g transform="translate(0,48) rotate(-90)">
        <circle r="22" fill="none" stroke="var(--blue)" stroke-width="15" pathLength="100" stroke-dasharray="40 100"/>
        <circle r="22" fill="none" stroke="var(--red)" stroke-width="15" pathLength="100" stroke-dasharray="60 100" stroke-dashoffset="-40"/>
      </g>
      <text class="pct" x="21" y="43">40%</text><text class="pct" x="-21" y="56.5">60%</text>
    </g>
    <g class="dots"><circle cx="183" cy="48" r="1.2"/><circle cx="187" cy="48" r="1.2"/><circle cx="191" cy="48" r="1.2"/></g>
    <g transform="translate(232,0)">
      <text class="chart-title" x="0" y="6">60/40</text>
      <circle cx="-12" cy="12" r="1.5" fill="var(--blue)"/><text class="legend" x="-9" y="13.3">Stocks</text>
      <circle cx="4" cy="12" r="1.5" fill="var(--red)"/><text class="legend" x="7" y="13.3">Bonds</text>
      <g transform="translate(0,48) rotate(-90)">
        <circle r="22" fill="none" stroke="var(--red)" stroke-width="15" pathLength="100" stroke-dasharray="40 100"/>
        <circle r="22" fill="none" stroke="var(--blue)" stroke-width="15" pathLength="100" stroke-dasharray="60 100" stroke-dashoffset="-40"/>
      </g>
      <text class="pct" x="21" y="43">40%</text><text class="pct" x="-21" y="56.5">60%</text>
    </g>
    <g class="dots"><circle cx="271" cy="48" r="1.2"/><circle cx="275" cy="48" r="1.2"/><circle cx="279" cy="48" r="1.2"/></g>
    <g transform="translate(321,0)">
      <text class="chart-title" x="0" y="6">80/20</text>
      <circle cx="-12" cy="12" r="1.5" fill="var(--blue)"/><text class="legend" x="-9" y="13.3">Stocks</text>
      <circle cx="4" cy="12" r="1.5" fill="var(--red)"/><text class="legend" x="7" y="13.3">Bonds</text>
      <g transform="translate(0,48) rotate(-90)">
        <circle r="22" fill="none" stroke="var(--red)" stroke-width="15" pathLength="100" stroke-dasharray="80 100"/>
        <circle r="22" fill="none" stroke="var(--blue)" stroke-width="15" pathLength="100" stroke-dasharray="20 100" stroke-dashoffset="-80"/>
      </g>
      <text class="pct" x="13" y="67.5">80%</text><text class="pct" x="-13" y="32">20%</text>
    </g>
  </svg>

  <h3 class="section-bar bar-tilt">TILT TO YOUR PREFERENCES</h3>
  <svg class="tilt-charts" width="370" height="120" viewBox="0 0 370 120">
    <g transform="translate(66,0)">
      <text class="chart-title" x="0" y="6">INTERNATIONAL</text>
      <circle cx="-36" cy="12" r="1.5" fill="var(--blue)"/><text class="legend" x="-33" y="13.3">Intl Stocks</text>
      <circle cx="4" cy="12" r="1.5" fill="var(--red)"/><text class="legend" x="7" y="13.3">Domestic Stocks</text>
      <circle cx="-36" cy="19" r="1.5" fill="var(--green)"/><text class="legend" x="-33" y="20.3">Govt Bonds</text>
      <circle cx="4" cy="19" r="1.5" fill="var(--purple)"/><text class="legend" x="7" y="20.3">Corp Bonds</text>
      <g transform="translate(0,74) rotate(-90)">
        <circle r="28" fill="none" stroke="var(--blue)" stroke-width="20" pathLength="100" stroke-dasharray="56 100"/>
        <circle r="28" fill="none" stroke="var(--red)" stroke-width="20" pathLength="100" stroke-dasharray="28 100" stroke-dashoffset="-56"/>
        <circle r="28" fill="none" stroke="var(--green)" stroke-width="20" pathLength="100" stroke-dasharray="8 100" stroke-dashoffset="-84"/>
        <circle r="28" fill="none" stroke="var(--purple)" stroke-width="20" pathLength="100" stroke-dasharray="8 100" stroke-dashoffset="-92"/>
      </g>
      <text class="pct" x="27.5" y="81">56%</text><text class="pct" x="-26.6" y="84.5">28%</text>
      <text class="pct pct-small" x="-19.2" y="55">8%</text><text class="pct pct-small" x="-7" y="48.3">8%</text>
    </g>
    <g class="dots"><circle cx="119" cy="74" r="1.2"/><circle cx="123" cy="74" r="1.2"/><circle cx="127" cy="74" r="1.2"/></g>
    <g transform="translate(185,0)">
      <text class="chart-title" x="0" y="6">SOCIALLY-RESPONSIBLE</text>
      <circle cx="-36" cy="12" r="1.5" fill="var(--blue)"/><text class="legend" x="-33" y="13.3">ESG</text>
      <circle cx="4" cy="12" r="1.5" fill="var(--red)"/><text class="legend" x="7" y="13.3">Stocks</text>
      <circle cx="-36" cy="19" r="1.5" fill="var(--green)"/><text class="legend" x="-33" y="20.3">Govt Bonds</text>
      <circle cx="4" cy="19" r="1.5" fill="var(--purple)"/><text class="legend" x="7" y="20.3">Corp Bonds</text>
      <g transform="translate(0,74) rotate(-90)">
        <circle r="28" fill="none" stroke="var(--blue)" stroke-width="20" pathLength="100" stroke-dasharray="45 100"/>
        <circle r="28" fill="none" stroke="var(--red)" stroke-width="20" pathLength="100" stroke-dasharray="27 100" stroke-dashoffset="-45"/>
        <circle r="28" fill="none" stroke="var(--green)" stroke-width="20" pathLength="100" stroke-dasharray="15 100" stroke-dashoffset="-72"/>
        <circle r="28" fill="none" stroke="var(--purple)" stroke-width="20" pathLength="100" stroke-dasharray="13 100" stroke-dashoffset="-87"/>
      </g>
      <text class="pct" x="27.7" y="71.3">45%</text><text class="pct" x="-14.3" y="99.8">27%</text>
      <text class="pct" x="-26.9" y="67.9">15%</text><text class="pct" x="-11.1" y="50">13%</text>
    </g>
    <g class="dots"><circle cx="238" cy="74" r="1.2"/><circle cx="242" cy="74" r="1.2"/><circle cx="246" cy="74" r="1.2"/></g>
    <g transform="translate(303,0)">
      <text class="chart-title" x="0" y="6">DIVIDEND</text>
      <circle cx="-36" cy="12" r="1.5" fill="var(--blue)"/><text class="legend" x="-33" y="13.3">Dividend Payers</text>
      <circle cx="4" cy="12" r="1.5" fill="var(--red)"/><text class="legend" x="7" y="13.3">Stocks</text>
      <circle cx="-36" cy="19" r="1.5" fill="var(--green)"/><text class="legend" x="-33" y="20.3">Govt Bonds</text>
      <circle cx="4" cy="19" r="1.5" fill="var(--purple)"/><text class="legend" x="7" y="20.3">Corp Bonds</text>
      <g transform="translate(0,74) rotate(-90)">
        <circle r="28" fill="none" stroke="var(--blue)" stroke-width="20" pathLength="100" stroke-dasharray="65 100"/>
        <circle r="28" fill="none" stroke="var(--red)" stroke-width="20" pathLength="100" stroke-dasharray="25 100" stroke-dashoffset="-65"/>
        <circle r="28" fill="none" stroke="var(--green)" stroke-width="20" pathLength="100" stroke-dasharray="5 100" stroke-dashoffset="-90"/>
        <circle r="28" fill="none" stroke="var(--purple)" stroke-width="20" pathLength="100" stroke-dasharray="5 100" stroke-dashoffset="-95"/>
      </g>
      <text class="pct" x="24.9" y="88.4">65%</text><text class="pct" x="-27.7" y="71.3">25%</text>
      <text class="pct pct-small" x="-12.7" y="50.6">5%</text><text class="pct pct-small" x="-4.4" y="47.8">5%</text>
    </g>
  </svg>

  <aside class="freedom">
    <h2>PROVIDING FINANCIAL FREEDOM</h2>
    <p>Lorem ipsum dolor sit amet, consectetuer adipiscing elit, sed diam nonummy nibh euismod tincidunt ut laoreet dolore magna aliquam erat volutpat. Ut wisi enim ad minim veniam, quis nostrud exerci tation ullamcorper suscipit lobortis nisl ut aliquip ex ea commodo consequat.</p>
    <p>Duis autem vel eum iriure dolor in hendrerit in vulputate velit esse molestie consequat, vel illum dolore eu feugiat nulla facilisis at vero eros et accumsan et iusto odio dignissim qui blandit praesent luptatum zzril</p>
  </aside>

  <div class="rule"></div>

  <footer>
    <div class="brand">
      <span class="brand-mark"></span>
      <span class="brand-name">Harbor Retirement Planning</span>
    </div>
    <div class="contact">
      <div class="phone">
        <svg width="14" height="16" viewBox="0 0 14 16" aria-hidden="true"><rect x="3" y="1" width="9" height="14" rx="2" fill="none" stroke="#fff" stroke-width="1.6"/><rect x="5.5" y="12" width="4" height="1.2" fill="#fff"/></svg>
        <span>(555) 014-2290</span>
      </div>
      <div class="web">www.harborretire.com</div>
    </div>
  </footer>
</main>
</body>
</html>
```